High End Business Card Design for Flooring Store

Looking for a new card design for our hardwood flooring company. We have no print budget for these and are open to cards made from wood, metal, cardstock with embossed print ... or any combination of these. No plastic.

We sell luxury products and I want the cards to reflect our image of quality and class.

Our contact information as such;
Employee Name
418 Colbrook Blvd.
Carrow Falls, NS
K9R-3M5
(555) 214-3968
Employee email @velkaflooring.com

Target Market(s)

Home Builders

Contact Information for Business Card

Emnployee name, business contact information

```html
<!DOCTYPE html>
<html lang="en">
<head>
<meta charset="utf-8">
<title>Velka Flooring – Business Card</title>
<link rel="stylesheet" href="https://fonts.googleapis.com/css2?family=Montserrat:wght@400;500;800&display=swap">
<style>
  :root {
    --page-bg: #8a8a8c;
    --brand-red: #9b2d24;
    --name-red: #8e2a20;
    --gold: #e2ac2a;
    --ink: #4a4a4a;
    --tagline-light: #bdb6ab;
    --tagline-dark: #555555;
    --card-white: #ffffff;
    --wood-dark: #33210f;
    --wood-mid: #5e3c1c;
    --wood-light: #7e5428;
  }
  * { margin: 0; padding: 0; box-sizing: border-box; }
  html, body { width: 900px; height: 1200px; overflow: hidden; }
  body {
    background: var(--page-bg);
    font-family: "Montserrat", sans-serif;
    position: relative;
  }
  .card { position: absolute; width: 632px; height: 362px; overflow: hidden; }
  .card-front { left: 134px; top: 212px; }
  .card-back { left: 135px; top: 628px; width: 631px; height: 360px; background: var(--card-white); }

  .wood-surface {
    position: absolute; inset: 0;
    background: radial-gradient(ellipse at 50% 85%, var(--wood-light) 0%, var(--wood-mid) 45%, var(--wood-dark) 100%);
  }
  .front-brand {
    position: absolute; left: 0; right: 0; top: 112px;
    text-align: center; color: var(--brand-red);
    font-weight: 500; font-size: 98px; line-height: 1; letter-spacing: 1px;
  }
  .front-tagline {
    position: absolute; left: 0; right: 0; top: 202px;
    text-align: center; color: var(--tagline-light);
    font-size: 23px; line-height: 28px; font-weight: 400;
  }

  .back-brand {
    position: absolute; right: 28px; top: 18px; width: 300px;
    text-align: center;
  }
  .back-brand .wordmark {
    color: var(--brand-red); font-weight: 500;
    font-size: 66px; line-height: 1; letter-spacing: 1px;
  }
  .back-brand .tagline {
    color: var(--tagline-dark); font-size: 17px; line-height: 19px; margin-top: 4px;
  }
  .person { position: absolute; left: 28px; top: 190px; }
  .person .name {
    color: var(--name-red); font-weight: 800; font-size: 23px;
    letter-spacing: 1px; line-height: 1;
  }
  .person .role { color: var(--ink); font-size: 15px; margin-top: 6px; letter-spacing: 0.5px; }
  .divider {
    position: absolute; left: 28px; right: 28px; top: 249px;
    height: 2px; background: var(--gold);
  }
  .contact-list {
    position: absolute; left: 28px; top: 267px; list-style: none;
  }
  .contact-list li {
    display: flex; align-items: center; height: 25px;
    color: var(--ink); font-size: 15px; letter-spacing: 1px;
  }
  .contact-list svg { width: 16px; height: 16px; margin-right: 10px; fill: var(--name-red); }
  .address {
    position: absolute; right: 28px; top: 267px; text-align: right;
    color: var(--ink); font-size: 15px; line-height: 25px; letter-spacing: 1px;
    font-style: normal;
  }
</style>
</head>
<body>

<section class="card card-front">
  <div class="wood-surface" role="img" aria-label="Photograph of a hardwood plank floor receding into the distance"></div>
  <div class="front-brand">Velka</div>
  <div class="front-tagline">Planchers &amp; Escaliers<br>Flooring &amp; Stairs</div>
</section>

<section class="card card-back">
  <div class="back-brand">
    <div class="wordmark">Velka</div>
    <div class="tagline">Planchers &amp; Escaliers<br>Flooring &amp; Stairs</div>
  </div>

  <div class="person">
    <div class="name">ALDEN MARSH</div>
    <div class="role">Sales</div>
  </div>

  <div class="divider"></div>

  <ul class="contact-list">
    <li>
      <svg viewBox="0 0 24 24" aria-hidden="true"><path d="M6.6 10.8a15.1 15.1 0 0 0 6.6 6.6l2.2-2.2a1 1 0 0 1 1-.25 11.4 11.4 0 0 0 3.6.57 1 1 0 0 1 1 1V20a1 1 0 0 1-1 1A17 17 0 0 1 3 4a1 1 0 0 1 1-1h3.5a1 1 0 0 1 1 1c0 1.25.2 2.45.57 3.57a1 1 0 0 1-.25 1z"/></svg>
      (555) 214-3968
    </li>
    <li>
      <svg viewBox="0 0 24 24" aria-hidden="true"><path d="M2 5h20v14H2z M3.5 6.5 12 12.5l8.5-6z" fill-rule="evenodd"/></svg>
      amarsh@velkaflooring.com
    </li>
    <li>
      <svg viewBox="0 0 24 24" aria-hidden="true"><path d="M12 2a10 10 0 1 0 0 20 10 10 0 0 0 0-20zm-1 2.1V8H7.3A8 8 0 0 1 11 4.1zm2 0A8 8 0 0 1 16.7 8H13zM4.5 10h6.5v4H4.5a8 8 0 0 1 0-4zm8.5 0h6.5a8 8 0 0 1 0 4H13zm-5.7 6H11v3.9A8 8 0 0 1 7.3 16zm5.7 0h3.7a8 8 0 0 1-3.7 3.9z"/></svg>
      www.velkaflooring.com
    </li>
  </ul>

  <address class="address">
    418 Colbrook Blvd.<br>
    Carrow Falls, NS<br>
    K9R-3M5
  </address>
</section>

</body>
</html>
```